Apartment services app

The app should permit current residents to pay rent, submit work orders or submit comments and general requests. There is an app that is available from Heron Works in the UK that could be used to benchmark, but I would like to see something more appropriate for the US.
Updates

The company name for this project is Oakvale Property Management. We will be providing a logo at a later date as we we will be submitting a separate design project for the development of a new logo.

Reason: I am extending the deadline by another week so that I may comment on the designs so far and each of you will have time to respond Tim

Target Market(s)

Residents of our apartment communities

Industry/Entity Type

Apartment

Requirements
Must have
• Ability to pay rent
• Ability to have reminders sent to resident
• Notices sent to resident
• Resident able to submit work order requests
• Resident able to submit comments and complaints

```html
<!DOCTYPE html>
<html lang="en">
<head>
<meta charset="utf-8">
<title>Oakvale Property Management – Resident App Screens</title>
<link rel="stylesheet" href="https://fonts.googleapis.com/css2?family=Roboto+Condensed:wght@400;500;700&family=Roboto:wght@400;500;700&display=swap">
<style>
  :root{
    --page:#ffffff;
    --status-bar:#3b4147;
    --status-text:#ffffff;
    --sky-light:#f2fbfe;
    --sky-mid:#b6e8f8;
    --sky-deep:#6fcdee;
    --header-blue:#1d62a6;
    --header-blue-dark:#15508c;
    --brand-blue:#2b8fd1;
    --button-ring:#2aa9e2;
    --button-fill-top:#d9f4fd;
    --button-fill-bottom:#6fcdf1;
    --button-active-top:#3aa8ea;
    --button-active-bottom:#1577c8;
    --icon-blue:#1d5a92;
    --label-dark:#1e3550;
    --city-blue:#4d8fc0;
    --city-faint:#8fd3ee;
  }
  *{box-sizing:border-box;margin:0;padding:0}
  html,body{width:1200px;height:860px;overflow:hidden;background:var(--page)}
  body{position:relative;font-family:"Roboto",Arial,sans-serif}

  .screen{position:absolute;overflow:hidden}
  .status-bar{position:absolute;left:0;top:0;width:100%;background:var(--status-bar);color:var(--status-text);display:flex;align-items:center;justify-content:center;font-family:"Roboto",Arial,sans-serif;font-weight:500}
  .status-bar .signal{position:absolute;left:8px;display:flex;align-items:flex-end;gap:2px}
  .status-bar .signal span{background:var(--status-text);display:block}
  .status-bar .battery{position:absolute;right:10px;border:2px solid var(--status-text);border-radius:2px}
  .status-bar .battery::after{content:"";position:absolute;right:-5px;top:30%;width:3px;height:40%;background:var(--status-text)}
  .status-bar .battery i{position:absolute;left:2px;top:2px;bottom:2px;width:45%;background:var(--status-text)}

  /* Splash screen */
  .splash{left:45px;top:185px;width:325px;height:485px;background:radial-gradient(ellipse at 45% 38%,var(--sky-light) 0%,var(--sky-mid) 55%,var(--sky-deep) 100%)}
  .splash .status-bar{height:21px;font-size:14px}
  .splash .status-bar .signal span{width:2px}
  .splash .status-bar .battery{width:18px;height:10px}
  .splash-brand{position:absolute;left:0;right:0;top:196px;text-align:center;font-family:"Roboto Condensed",Arial,sans-serif;font-weight:500;color:var(--brand-blue);font-size:20px;line-height:24px;white-space:nowrap}
  .splash-city{position:absolute;left:0;bottom:0;width:100%;height:200px;background:linear-gradient(to bottom,rgba(77,143,192,0) 0%,rgba(77,143,192,.55) 35%,var(--city-blue) 100%)}

  /* Menu screen */
  .menu{left:587px;top:12px;width:553px;height:831px;background:radial-gradient(ellipse at 48% 40%,var(--sky-light) 0%,var(--sky-mid) 60%,var(--sky-deep) 100%)}
  .menu .status-bar{height:35px;font-size:22px;font-weight:700}
  .menu .status-bar .signal span{width:4px}
  .menu .status-bar .battery{width:30px;height:16px}
  .app-header{position:absolute;left:0;top:35px;width:100%;height:80px;background:linear-gradient(to bottom,var(--header-blue) 0%,var(--header-blue-dark) 100%);display:flex;align-items:center;justify-content:center;padding-left:60px}
  .app-title{font-family:"Roboto Condensed",Arial,sans-serif;font-weight:500;font-size:27px;color:#fff;letter-spacing:.2px;white-space:nowrap}
  .menu-city{position:absolute;left:0;bottom:0;width:100%;height:250px;background:linear-gradient(to bottom,rgba(143,211,238,0) 0%,rgba(120,196,232,.6) 45%,var(--city-faint) 100%)}

  .menu-button{position:absolute;width:120px;height:120px;border-radius:50%;border:4px solid var(--button-ring);background:radial-gradient(circle at 50% 28%,var(--button-fill-top) 0%,var(--button-fill-bottom) 100%);box-shadow:0 3px 8px rgba(20,90,140,.3)}
  .menu-button::before{content:"";position:absolute;inset:5px;border-radius:50%;border:2px dashed rgba(255,255,255,.9)}
  .menu-button.is-active{background:radial-gradient(circle at 50% 28%,var(--button-active-top) 0%,var(--button-active-bottom) 100%)}
  .menu-button svg,.menu-button .icon-slot{position:absolute;left:50%;top:18px;transform:translateX(-50%)}
  .menu-button .label{position:absolute;left:0;right:0;bottom:16px;text-align:center;font-size:12.5px;color:var(--label-dark)}
  .menu-button.is-active .label{color:#fff}
  .icon-slot{width:54px;height:56px;border-radius:50% 50% 8px 8px;background:linear-gradient(to bottom,#2f6fa6,#1d5a92)}

  .work-order{left:118px;top:153px}
  .rent{left:318px;top:153px}
  .alerts{left:120px;top:313px}
  .message{left:320px;top:313px}
  .program{left:113px;top:478px}
  .contact{left:321px;top:478px}
</style>
</head>
<body>

<section class="screen splash" aria-label="Splash screen">
  <div class="status-bar">
    <div class="signal"><span style="height:3px"></span><span style="height:4px"></span><span style="height:5px"></span><span style="height:7px"></span><span style="height:8px"></span></div>
    4:20 PM
    <div class="battery"><i></i></div>
  </div>
  <div class="splash-brand">Oakvale Property Management</div>
  <div class="splash-city" role="img" aria-label="City skyline of high-rise apartment towers in blue"></div>
</section>

<section class="screen menu" aria-label="Resident menu screen">
  <div class="status-bar">
    <div class="signal"><span style="height:5px"></span><span style="height:8px"></span><span style="height:11px"></span><span style="height:14px"></span><span style="height:17px"></span></div>
    4:20 PM
    <div class="battery"><i></i></div>
  </div>
  <header class="app-header"><h1 class="app-title">Oakvale Property Management</h1></header>
  <div class="menu-city" role="img" aria-label="Faint city skyline of apartment towers"></div>

  <div class="menu-button work-order is-active">
    <svg width="56" height="56" viewBox="0 0 56 56" aria-hidden="true">
      <path d="M14 6h28l-4 40H10z" fill="#fff"/>
      <path d="M10 46c-4 0-6-3-5-6h33c-1 4-2 6-6 6z" fill="#e6f3fb"/>
      <g fill="#1d5a92"><rect x="18" y="13" width="4" height="4"/><rect x="24" y="14" width="13" height="2"/><rect x="17" y="21" width="4" height="4"/><rect x="23" y="22" width="13" height="2"/><rect x="16" y="29" width="4" height="4"/><rect x="22" y="30" width="13" height="2"/></g>
    </svg>
    <span class="label">Work Order</span>
  </div>

  <div class="menu-button rent">
    <svg width="56" height="56" viewBox="0 0 56 56" aria-hidden="true">
      <text x="28" y="26" text-anchor="middle" font-family="Roboto,Arial,sans-serif" font-weight="700" font-size="28" fill="#1d5a92">$</text>
      <path d="M6 34h12l8 4h14l8-6 3 2-9 12H6z" fill="#1d5a92"/>
    </svg>
    <span class="label">Rent</span>
  </div>

  <div class="menu-button alerts">
    <svg width="56" height="56" viewBox="0 0 56 56" aria-hidden="true">
      <circle cx="28" cy="8" r="4" fill="#1d5a92"/>
      <path d="M16 38c2-4 2-10 2-16a10 10 0 0 1 20 0c0 6 0 12 2 16z" fill="#1d5a92"/>
      <ellipse cx="28" cy="39" rx="18" ry="5" fill="none" stroke="#1d5a92" stroke-width="3"/>
      <circle cx="28" cy="46" r="4" fill="#1d5a92"/>
    </svg>
    <span class="label">Alerts</span>
  </div>

  <div class="menu-button message">
    <svg width="56" height="56" viewBox="0 0 56 56" aria-hidden="true">
      <path d="M8 6h28a6 6 0 0 1 6 6v14a6 6 0 0 1-6 6H18l-8 7v-7a6 6 0 0 1-6-6V12a4 6 0 0 1 4-6z" fill="#1d5a92"/>
      <rect x="12" y="14" width="20" height="3" fill="#bfe8f8"/><rect x="12" y="21" width="14" height="3" fill="#bfe8f8"/>
      <path d="M44 20h4a5 5 0 0 1 5 5v12a5 5 0 0 1-5 5v6l-7-6H34a5 5 0 0 1-5-5v-1h9a6 6 0 0 0 6-6z" fill="#1d5a92"/>
    </svg>
    <span class="label">Message</span>
  </div>

  <div class="menu-button program">
    <svg width="56" height="56" viewBox="0 0 56 56" aria-hidden="true">
      <g fill="#1d5a92"><path d="M4 4h20v20H10a6 6 0 0 1-6-6z"/><path d="M32 4h20v14a6 6 0 0 1-6 6H32z"/><path d="M4 32h20v20H10a6 6 0 0 1-6-6z"/><path d="M32 32h14a6 6 0 0 1 6 6v14H32z"/></g>
    </svg>
    <span class="label">Program</span>
  </div>

  <div class="menu-button contact">
    <div class="icon-slot" role="img" aria-label="Contact person symbol"></div>
    <span class="label">Contact</span>
  </div>
</section>

</body>
</html>
```